Business Card Design Project

Im an electrician and my company name is Kestrel Electrical
My main work is installing Lighting and Power Points, Home Theater Systems, TVS, Phones and Data
Im looking a business card, something nice, clean, modern and not to cluttered
Im open to sugestions
I dont mind if the "Services" is on the back on the business card
colours black, grey, white or the blue colour of my logo are prefered but not compulsory
any questions just message me
and please make it so if i need to edit the writing can do it easy. maybe by making it a seperate layer ?
My Details are.
Name - Peter Halloran
Job Title - Licenced Electrician
Mobile - 027 583 2174
Email - peter@kestrelelectrical.co.nz
Web - www.kestrelelectrical.co.nz
Services
Residential / Commercial
Lighting & Power
Heating & Ventilation
Automation
Phone & Data
Home Cinema
Sound Systems
TV, Antenna & Satellite
Digital Upgrades

```html
<!DOCTYPE html>
<html lang="en">
<head>
<meta charset="utf-8">
<title>Kestrel Electrical – Business Card</title>
<link href="https://fonts.googleapis.com/css2?family=Open+Sans:wght@300;400;600;700&display=swap" rel="stylesheet">
<style>
  :root {
    --teal: #16b3cf;
    --teal-deep: #0e7f8f;
    --teal-mid: #1a9aa8;
    --slate: #5b6770;
    --paper: #ffffff;
    --paper-shade: #eef0f2;
    --stage: #d9dcdf;
    --glow: #dff8ff;
  }
  * { margin: 0; padding: 0; box-sizing: border-box; }
  html, body {
    width: 1200px; height: 960px; overflow: hidden;
    background: var(--stage);
    font-family: "Open Sans", Arial, sans-serif;
  }
  .sheet {
    width: 1200px; height: 960px;
    display: flex; flex-direction: column; align-items: center; justify-content: center;
    gap: 50px;
  }
  .card {
    position: relative;
    width: 700px; height: 400px;
    overflow: hidden;
    box-shadow: 0 10px 30px rgba(0,0,0,0.18);
  }

  /* Front */
  .card-front {
    background: linear-gradient(160deg, var(--paper) 45%, var(--paper-shade) 100%);
  }
  .front-wordmark {
    position: absolute; left: 60px; top: 60px;
    display: flex; align-items: center; gap: 14px;
  }
  .mark-square {
    width: 46px; height: 46px; background: var(--teal);
  }
  .wordmark-text {
    font-weight: 600; font-size: 34px; letter-spacing: 1.5px;
    color: var(--teal); line-height: 1.05;
    text-transform: uppercase;
  }
  .person {
    position: absolute; left: 60px; top: 200px;
  }
  .person-name {
    font-weight: 600; font-size: 40px; color: var(--slate); line-height: 1.1;
  }
  .person-title {
    font-weight: 400; font-style: italic; font-size: 20px; color: var(--teal);
    letter-spacing: 0.5px;
  }
  .contact {
    position: absolute; left: 60px; top: 300px;
    list-style: none;
  }
  .contact li {
    display: flex; align-items: center; gap: 12px;
    font-size: 20px; color: var(--slate); line-height: 36px;
  }
  .contact svg { width: 22px; height: 22px; fill: var(--teal); }
  .front-web {
    position: absolute; right: 40px; top: 290px;
    font-weight: 600; font-size: 19px; color: var(--teal);
  }

  /* Back */
  .card-back { color: var(--paper); }
  .back-art {
    position: absolute; inset: 0;
    background:
      radial-gradient(ellipse at 75% 30%, rgba(223,248,255,0.45), transparent 55%),
      linear-gradient(135deg, var(--teal-deep) 0%, var(--teal-mid) 55%, var(--teal-deep) 100%);
  }
  .back-content {
    position: absolute; right: 40px; top: 70px; width: 440px;
    text-align: center;
  }
  .back-wordmark {
    font-weight: 600; font-size: 30px; letter-spacing: 2px;
    text-transform: uppercase; color: var(--paper);
    display: flex; align-items: center; justify-content: center; gap: 12px;
  }
  .back-wordmark .mark-square { width: 36px; height: 36px; background: var(--paper); }
  .sector {
    margin-top: 34px;
    font-size: 25px; font-weight: 400; letter-spacing: 0.5px;
  }
  .services {
    margin-top: 10px;
    font-size: 15.5px; line-height: 1.55; letter-spacing: 0.3px;
  }
  .services .sep { color: var(--glow); opacity: 0.6; margin: 0 6px; }
</style>
</head>
<body>
<main class="sheet">

  <section class="card card-front" aria-label="Business card front">
    <div class="front-wordmark">
      <span class="mark-square"></span>
      <span class="wordmark-text">Kestrel<br>Electrical</span>
    </div>

    <div class="person">
      <h1 class="person-name">Peter Halloran</h1>
      <p class="person-title">Licenced Electrician</p>
    </div>

    <ul class="contact">
      <li>
        <svg viewBox="0 0 24 24" aria-hidden="true"><path d="M7 1h10a2 2 0 0 1 2 2v18a2 2 0 0 1-2 2H7a2 2 0 0 1-2-2V3a2 2 0 0 1 2-2zm0 3v13h10V4H7zm5 15a1.2 1.2 0 1 0 0 2.4A1.2 1.2 0 0 0 12 19z"/></svg>
        <span>027 583 2174</span>
      </li>
      <li>
        <svg viewBox="0 0 24 24" aria-hidden="true"><path d="M2 5h20v14H2V5zm2 2v.4l8 5.2 8-5.2V7H4zm0 2.8V17h16V9.8l-8 5.2-8-5.2z"/></svg>
        <span>peter@kestrelelectrical.co.nz</span>
      </li>
    </ul>

    <p class="front-web">kestrelelectrical.co.nz</p>
  </section>

  <section class="card card-back" aria-label="Business card back">
    <div class="back-art" role="img" aria-label="Teal background with glowing circuit line graphic"></div>
    <div class="back-content">
      <div class="back-wordmark">
        <span class="mark-square"></span>
        <span>Kestrel Electrical</span>
      </div>
      <p class="sector">Residential/Commercial</p>
      <p class="services">
        Lighting &amp; Power<span class="sep">|</span>Heating &amp; Ventilation<span class="sep">|</span>Automation<br>
        Phone &amp; Data<span class="sep">|</span>Home Cinema<span class="sep">|</span>Sound Systems<br>
        TV, Antenna &amp; Satellite<span class="sep">|</span>Digital Upgrades
      </p>
    </div>
  </section>

</main>
</body>
</html>
```